Custom Soapstone Shower Floor Brochure

Brody, after some thought and a very close look at your services. I have decided to enter into a design agreement with ArtLoomly. The following task is what I need help with:

1) While using our logo develop a captivating, informative and attractive double sided brochure (that can be printed on standard high gloss paper (8 1/2" x 11") that will draw interest and attention to our product shower floors. Information at northridgeslabworks.com. I would like any one picking up the brochure (at a trade show for example) to want to ask questions regarding the product we are selling "shower floors". There should be text and photos. (I have attached a few samples)

I am leaving everything up to your creative team, scour the internet for information, re-write my text. Essentially come up with something that high end hotels and commercial clients will be drawn to.

Thanking you in advance,

Hal

Target Market(s)

Hotels, commercial condominium clients, non residential.

Industry/Entity Type

Commercial

Font styles to use
Other font styles liked:
• The logo is in Veranda font however we are no married to it.

Colors

Designer to choose colors to be used in the design.

Requirements
Must have
• Informative text and pictures describing our product in a way that it will want to make people ask more questions.
Nice to have
• Pictures showcasing the shower floors, I can send more pictures if allowed.
Should not have
• Extremely bright colors.

```html
<!DOCTYPE html>
<html lang="en">
<head>
<meta charset="utf-8">
<title>Northridge Slabworks – Shower Floor Brochure</title>
<link href="https://fonts.googleapis.com/css2?family=Open+Sans:wght@300;400;600;700;800&display=swap" rel="stylesheet">
<style>
  :root{
    --backdrop:#bdbdbd;
    --ink:#2e3340;
    --ink-deep:#232733;
    --paper:#ffffff;
    --paper-soft:#eceef2;
    --mist:#d9dce2;
    --text:#3a3d45;
    --text-light:#e8eaee;
    --muted:#8a8f99;
  }
  *{box-sizing:border-box;margin:0;padding:0}
  html,body{width:1200px;height:2441px;overflow:hidden}
  body{background:var(--backdrop);font-family:"Open Sans",Arial,sans-serif;color:var(--text);position:relative}

  .page{position:absolute;background:var(--paper);overflow:hidden;box-shadow:0 6px 18px rgba(0,0,0,.18)}
  .abs{position:absolute}

  .photo{position:absolute;background:linear-gradient(160deg,#f4f5f7 0%,#d3d6db 45%,#9a9ea6 75%,#6b5a4a 100%)}
  .photo--stone{background:linear-gradient(135deg,#c6ccd4 0%,#8f98a4 50%,#6f7884 100%)}
  .photo--room{background:linear-gradient(170deg,#eef0f3 0%,#c9cdd3 55%,#7d838d 100%)}
  .photo--framed{border:5px solid var(--paper)}

  /* brand */
  .brand{position:absolute;text-align:center;color:var(--ink)}
  .brand__dot{display:block;border-radius:50%;background:var(--ink);margin:0 auto}
  .brand__name{display:block;font-weight:400;letter-spacing:.3px}
  .brand__tag{display:block;color:var(--muted);font-weight:400}

  /* front cover */
  .cover{left:320px;top:70px;width:560px;height:725px;background:linear-gradient(180deg,#f1f2f5 0%,#ffffff 25%)}
  .cover .brand{left:0;right:0;top:34px}
  .cover .brand__dot{width:40px;height:40px;margin-bottom:10px}
  .cover .brand__name{font-size:25px}
  .cover .brand__tag{font-size:12px;margin-top:4px}
  .cover__band{left:32px;top:160px;width:48px;height:360px;background:var(--ink)}
  .cover__photo{left:80px;top:160px;width:480px;height:360px}
  .cover__rule{left:80px;top:540px;width:3px;height:50px;background:var(--ink)}
  .headline{left:92px;top:535px;color:var(--ink);line-height:1.15}
  .headline__light{display:block;font-size:17px;font-weight:400;letter-spacing:.2px}
  .headline__bold{display:block;font-size:23px;font-weight:800}
  .cover__body{left:92px;top:600px;width:430px;font-size:11.5px;line-height:1.45;color:var(--text)}
  .webbar{position:absolute;display:flex;align-items:center;gap:7px;background:var(--ink);color:var(--paper);font-size:12px;padding:0 14px}
  .cover .webbar{right:0;top:688px;height:24px;width:250px}
  .cover__line{left:0;top:699px;width:320px;height:2px;background:var(--ink)}

  /* outside spread */
  .back{left:60px;top:875px;width:540px;height:699px;background:radial-gradient(ellipse at 30% 10%,#ffffff 0%,#e4e6eb 60%,#d5d8de 100%)}
  .back .brand{left:40px;top:40px;text-align:left;display:flex;align-items:center;gap:10px}
  .back .brand__dot{width:26px;height:26px;margin:0}
  .back .brand__name{font-size:16px}
  .back .brand__tag{font-size:9px}
  .about{left:0;top:125px;width:495px;height:415px;background:var(--ink)}
  .about__title{left:26px;top:22px;color:var(--paper);font-size:23px;font-weight:700}
  .about__title span{font-weight:300}
  .about__intro{left:26px;top:62px;width:445px;font-size:9.5px;line-height:1.5;color:var(--text-light)}
  .about__col{left:26px;top:160px;width:200px;font-size:9.5px;line-height:1.55;color:var(--text-light)}
  .about__photo{left:240px;top:165px;width:225px;height:160px}
  .contact{left:34px;top:572px}
  .contact__title{font-size:21px;font-weight:700;color:var(--ink);margin-bottom:8px}
  .contact__title span{font-weight:300}
  .contact__row{display:flex;align-items:center;gap:8px;font-size:12px;color:var(--text);margin-bottom:4px}
  .social{right:50px;top:578px;display:flex;gap:5px}
  .social i{display:block;width:14px;height:14px;border:1.5px solid var(--ink);border-radius:50%}

  .front-mini{left:600px;top:875px;width:540px;height:699px;background:linear-gradient(180deg,#f1f2f5 0%,#ffffff 25%)}
  .front-mini .brand{left:0;right:0;top:32px}
  .front-mini .brand__dot{width:38px;height:38px;margin-bottom:9px}
  .front-mini .brand__name{font-size:24px}
  .front-mini .brand__tag{font-size:11px;margin-top:4px}
  .front-mini .cover__band{left:30px;top:152px;width:46px;height:348px}
  .front-mini .cover__photo{left:76px;top:152px;width:464px;height:348px}
  .front-mini .cover__rule{top:520px;height:48px}
  .front-mini .headline{top:515px;left:88px}
  .front-mini .headline__light{font-size:16px}
  .front-mini .headline__bold{font-size:22px}
  .front-mini .cover__body{left:88px;top:578px;width:415px;font-size:11px}
  .front-mini .webbar{right:0;top:664px;height:23px;width:240px;font-size:11.5px}
  .front-mini .cover__line{top:674px;width:300px}

  /* inside spread */
  .inside-left{left:60px;top:1654px;width:540px;height:699px;background:var(--ink)}
  .inside-left__photo{left:0;top:0;width:540px;height:300px}
  .section-bar{left:0;top:318px;width:330px;height:34px;background:var(--ink-deep);display:flex;align-items:center;padding-left:30px;color:var(--paper);font-size:17px;font-weight:700;letter-spacing:.5px}
  .section-bar::before{content:"";width:4px;height:20px;background:var(--paper);margin-right:12px}
  .inside-cols{left:30px;top:378px;width:480px;display:flex;gap:24px}
  .inside-cols p{flex:1;font-size:10px;line-height:1.6;color:var(--text-light)}
  .dropcap{float:left;font-size:44px;line-height:.9;font-weight:700;margin:2px 6px 0 0;color:var(--paper)}

  .inside-right{left:600px;top:1654px;width:540px;height:699px;background:var(--paper-soft)}
  .inside-right__intro{left:44px;top:32px;width:460px;font-size:10px;line-height:1.6;color:var(--text);padding-left:12px;border-left:3px solid var(--ink)}
  .collage-main{left:30px;top:130px;width:315px;height:430px}
  .collage-side{left:352px;width:158px;height:136px}
  .inside-right__outro{left:44px;top:585px;width:460px;font-size:10px;line-height:1.6;color:var(--text)}
</style>
</head>
<body>

<!-- Front cover -->
<section class="page cover">
  <div class="brand">
    <span class="brand__dot"></span>
    <span class="brand__name">Northridge Slabworks</span>
    <span class="brand__tag">Honed Stone Floors</span>
  </div>
  <div class="abs cover__band"></div>
  <div class="photo cover__photo" role="img" aria-label="Hotel bathroom with two vessel sinks on a wood vanity and grey soapstone walls"></div>
  <div class="abs cover__rule"></div>
  <h1 class="abs headline">
    <span class="headline__light">LOREM IPSUM DOLOR SIT AMET,</span>
    <span class="headline__bold">CONSECTETUR ADIPISCING ELIT</span>
  </h1>
  <p class="abs cover__body">Suspendisse id pretium turpis. Fusce viverra venenatis egestas. Suspendisse id pretium turpis. Fusce viverra venenatis egestas. In hac habitasse platea dictumst. Integer et tincidunt nulla.</p>
  <div class="abs cover__line"></div>
  <div class="webbar">
    <svg width="12" height="12" viewBox="0 0 12 12" fill="none" stroke="#fff" stroke-width="1"><circle cx="6" cy="6" r="5"/><ellipse cx="6" cy="6" rx="2.2" ry="5"/><line x1="1" y1="6" x2="11" y2="6"/></svg>
    www.northridgeslabworks.com
  </div>
</section>

<!-- Back cover -->
<section class="page back">
  <div class="brand">
    <span class="brand__dot"></span>
    <span><span class="brand__name">Northridge Slabworks</span><span class="brand__tag">Honed Stone Floors</span></span>
  </div>
  <div class="abs about">
    <h2 class="abs about__title">About <span>us</span></h2>
    <p class="abs about__intro">Northridge Slabworks shapes dense natural soapstone into seamless shower floors for hotels, condominiums and commercial spaces. The stone never stains, resists heat and stays warm underfoot, so every bathroom keeps its calm, polished look through years of daily guest traffic and careful cleaning.</p>
    <p class="abs about__col">Each floor is cut to measure in our shop, sloped for drainage and finished by hand. Soapstone is non porous, so water, soap and oils rinse away without sealers or harsh chemicals. Ask us for samples and pricing.</p>
    <div class="photo photo--stone photo--framed about__photo" role="img" aria-label="Grey soapstone shower wall with a pink orchid"></div>
  </div>
  <div class="social abs"><i></i><i></i><i></i><i></i><i></i><i></i></div>
  <div class="abs contact">
    <h3 class="contact__title">Get in <span>touch</span></h3>
    <div class="contact__row">
      <svg width="11" height="13" viewBox="0 0 11 13"><path d="M5.5 0C2.5 0 .5 2.2.5 4.8c0 3.4 5 8.2 5 8.2s5-4.8 5-8.2C10.5 2.2 8.5 0 5.5 0z" fill="#2e3340"/><circle cx="5.5" cy="4.8" r="1.7" fill="#fff"/></svg>
      2290 Cedar Hollow Road, Ashford
    </div>
    <div class="contact__row">
      <svg width="11" height="12" viewBox="0 0 24 24"><path d="M6.6 10.8a15 15 0 006.6 6.6l2.2-2.2c.3-.3.7-.4 1-.2 1.1.4 2.3.6 3.6.6.6 0 1 .4 1 1V20c0 .6-.4 1-1 1A17 17 0 013 4c0-.6.4-1 1-1h3.5c.6 0 1 .4 1 1 0 1.3.2 2.5.6 3.6.1.3 0 .7-.2 1z" fill="#2e3340"/></svg>
      555-014-2376
    </div>
    <div class="contact__row">
      <svg width="12" height="12" viewBox="0 0 12 12" fill="none" stroke="#2e3340" stroke-width="1"><circle cx="6" cy="6" r="5"/><ellipse cx="6" cy="6" rx="2.2" ry="5"/><line x1="1" y1="6" x2="11" y2="6"/></svg>
      www.northridgeslabworks.com
    </div>
  </div>
</section>

<!-- Front cover in spread -->
<section class="page front-mini">
  <div class="brand">
    <span class="brand__dot"></span>
    <span class="brand__name">Northridge Slabworks</span>
    <span class="brand__tag">Honed Stone Floors</span>
  </div>
  <div class="abs cover__band"></div>
  <div class="photo cover__photo" role="img" aria-label="Hotel bathroom with two vessel sinks on a wood vanity and grey soapstone walls"></div>
  <div class="abs cover__rule"></div>
  <h2 class="abs headline">
    <span class="headline__light">LOREM IPSUM DOLOR SIT AMET,</span>
    <span class="headline__bold">CONSECTETUR ADIPISCING ELIT</span>
  </h2>
  <p class="abs cover__body">Suspendisse id pretium turpis. Fusce viverra venenatis egestas. Suspendisse id pretium turpis. Fusce viverra venenatis egestas. In hac habitasse platea dictumst. Integer et tincidunt nulla.</p>
  <div class="abs cover__line"></div>
  <div class="webbar">
    <svg width="12" height="12" viewBox="0 0 12 12" fill="none" stroke="#fff" stroke-width="1"><circle cx="6" cy="6" r="5"/><ellipse cx="6" cy="6" rx="2.2" ry="5"/><line x1="1" y1="6" x2="11" y2="6"/></svg>
    www.northridgeslabworks.com
  </div>
</section>

<!-- Inside left -->
<section class="page inside-left">
  <div class="photo photo--room inside-left__photo" role="img" aria-label="Bathroom with soapstone floor, pedestal sink and toilet"></div>
  <h2 class="abs section-bar">LOREM IPSUM</h2>
  <div class="abs inside-cols">
    <p><span class="dropcap">L</span>uxury guests notice the floor first. A single soapstone slab replaces dozens of grout lines, giving every shower a quiet, unbroken surface that feels solid and safe. Its soft honed texture grips wet feet while the deep grey tones hide marks between cleanings.</p>
    <p>Because the stone is dense and chemically inert, it will not etch, crack from heat or harbour mould. Housekeeping teams simply rinse and wipe. Scratches can be sanded out on site, so the floor looks new for decades of service.</p>
  </div>
</section>

<!-- Inside right -->
<section class="page inside-right">
  <p class="abs inside-right__intro">From boutique hotels to large condominium towers, our shower floors are templated, cut and installed as one piece. We match every drain position, curb height and slope, then deliver a finished floor ready for tile or glass walls.</p>
  <div class="photo photo--room collage-main" role="img" aria-label="Bathroom with white vanity, mirror and grey soapstone floor"></div>
  <div class="photo photo--stone collage-side" style="top:130px" role="img" aria-label="Soapstone shower stall with glass door"></div>
  <div class="photo photo--room collage-side" style="top:277px" role="img" aria-label="Compact bathroom with toilet on soapstone floor"></div>
  <div class="photo photo--stone collage-side" style="top:424px" role="img" aria-label="Soapstone shower bench and floor"></div>
  <p class="abs inside-right__outro">Visit our showroom to feel the stone, compare finishes and talk with our team about lead times, project volume and custom shapes for your next commercial build.</p>
</section>

</body>
</html>
```